Automotive component supplier needs a business card design

We need a business card design for our company called Velmar Global Components Ltd based in the UK. We are a supplier of interior and exterior components to premium car manufacturers such as Corvane Hale, Durrant Fyfe, Maxtorn and Valdessimo. We would like to see a modern business card design that uses the colour blue.

Target Market(s)

Premium automotive car manufacturers.

Industry/Entity Type

Automotive

Contact Information for Business Card

Company Name : Velmar Global Components Limited
Address: 17 Tamsey Yard, Upper Drisk, Warwick, CV31 8RJ, United Kingdom
Web Address : www.velmarparts-example.co.uk

Font styles to use
Other font styles liked:
• Helvetica

Colors
3176b5
0255a3
85acd3
cfdeed
cee9f5
85cae6
34a6d7
0692cd
9bcb3c

Requirements
Must have
• Clear company logo and a mixture of blue colours.
Nice to have
• A high quality modern image.
Should not have
• Multiple colours.

```html
<!DOCTYPE html>
<html lang="en">
<head>
<meta charset="utf-8">
<title>Velmar Global Components – Business Card</title>
<link href="https://fonts.googleapis.com/css2?family=Arimo:wght@400;700&display=swap" rel="stylesheet">
<style>
  :root {
    --page: #e4e4e4;
    --card: #ffffff;
    --brand-blue: #0692cd;
    --line-blue: #34a6d7;
    --ink: #1f2a2a;
    --ink-soft: #3a3a3a;
  }
  * { margin: 0; padding: 0; box-sizing: border-box; }
  html, body { width: 1200px; height: 1200px; overflow: hidden; }
  body {
    background: var(--page);
    font-family: "Arimo", Helvetica, Arial, sans-serif;
    display: flex;
    flex-direction: column;
    align-items: center;
    justify-content: center;
    gap: 60px;
  }
  .card {
    position: relative;
    width: 840px;
    height: 480px;
    background: var(--card);
    box-shadow: 0 6px 18px rgba(0,0,0,0.12);
  }
  .brand {
    position: absolute;
    left: 0; right: 0;
    display: flex;
    justify-content: center;
    color: var(--brand-blue);
    font-weight: 700;
    text-transform: uppercase;
  }
  .brand__lockup { display: inline-flex; flex-direction: column; align-items: stretch; }
  .brand__name { font-size: 120px; line-height: 1; letter-spacing: 2px; }
  .brand__sub {
    font-size: 26px;
    line-height: 1.2;
    margin-top: 6px;
    display: flex;
    justify-content: space-between;
  }

  .card--back .brand { top: 125px; }
  .card--front .brand { top: 70px; }

  .holder {
    position: absolute;
    right: 468px;
    top: 330px;
    text-align: right;
  }
  .holder__name { font-size: 30px; color: var(--ink); }
  .holder__role { font-size: 22px; color: var(--brand-blue); margin-top: 2px; }

  .divider {
    position: absolute;
    left: 392px; top: 285px;
    width: 3px; height: 150px;
    background: var(--line-blue);
  }

  .contacts {
    position: absolute;
    left: 415px; top: 282px;
    list-style: none;
    font-size: 20px;
    color: var(--ink-soft);
  }
  .contacts li { display: flex; align-items: center; gap: 12px; height: 34px; }
  .contacts svg { width: 22px; height: 22px; flex: none; }

  .address {
    position: absolute;
    left: 0; right: 0; bottom: 60px;
    text-align: center;
    font-size: 20px;
    color: var(--ink-soft);
  }
</style>
</head>
<body>

  <section class="card card--back" aria-label="Business card, back">
    <div class="brand">
      <div class="brand__lockup">
        <span class="brand__name">Velmar</span>
        <span class="brand__sub"><span>Global</span><span>Components</span></span>
      </div>
    </div>
    <p class="address">17 Tamsey Yard, Upper Drisk, Warwick, CV31 8RJ, United Kingdom</p>
  </section>

  <section class="card card--front" aria-label="Business card, front">
    <div class="brand">
      <div class="brand__lockup">
        <span class="brand__name">Velmar</span>
        <span class="brand__sub"><span>Global</span><span>Components</span></span>
      </div>
    </div>

    <div class="holder">
      <p class="holder__name">Elsa Rendhall</p>
      <p class="holder__role">Owner</p>
    </div>

    <div class="divider"></div>

    <ul class="contacts">
      <li>
        <svg viewBox="0 0 22 22" aria-hidden="true"><rect width="22" height="22" rx="3" fill="#0692cd"/><path d="M6 5h3l1 3-2 1.5a8 8 0 0 0 4.5 4.5L14 12l3 1v3c0 .6-.4 1-1 1A11 11 0 0 1 5 6c0-.6.4-1 1-1z" fill="#fff"/></svg>
        0455 318 907
      </li>
      <li>
        <svg viewBox="0 0 22 22" aria-hidden="true"><rect width="22" height="22" rx="3" fill="#0692cd"/><rect x="7" y="4" width="8" height="14" rx="1.5" fill="#fff"/><rect x="8.5" y="6" width="5" height="8" fill="#0692cd"/></svg>
        7013829064
      </li>
      <li>
        <svg viewBox="0 0 22 22" aria-hidden="true"><rect width="22" height="22" rx="3" fill="#0692cd"/><rect x="4" y="6" width="14" height="10" fill="#fff"/><path d="M4 6l7 6 7-6" fill="none" stroke="#0692cd" stroke-width="1.5"/></svg>
        hello@velmarparts-example.com
      </li>
      <li>
        <svg viewBox="0 0 22 22" aria-hidden="true"><rect width="22" height="22" rx="3" fill="#0692cd"/><circle cx="11" cy="11" r="6.5" fill="none" stroke="#fff" stroke-width="1.5"/><ellipse cx="11" cy="11" rx="3" ry="6.5" fill="none" stroke="#fff" stroke-width="1.2"/><path d="M4.5 11h13" stroke="#fff" stroke-width="1.2"/></svg>
        www.velmarparts-example.co.uk
      </li>
    </ul>
  </section>

</body>
</html>
```